Business card with logo for a family psychologist

I need a business card for my private practice in the urban Chicago area as a psychologist. I see families and individuals who are going through difficult times - divorce, separation, illness, or trauma. I want to project hopefulness, competence, and caring.

Target Market(s)

Adults, other professionals - such as physicans and lawyers

Industry/Entity Type

Health Care

Contact Information for Business Card

Front should have my name and credentials; back should have location information including my email, phone

Font styles to use
Serif
Decorative
Script

Requirements
Must have
• Unique logo
Should not have
• No pictures or icons of people; no black

```html
<!DOCTYPE html>
<html lang="en">
<head>
<meta charset="utf-8">
<title>Dr. Laurel Hayes – Business Card</title>
<link rel="stylesheet" href="https://fonts.googleapis.com/css2?family=Cinzel:wght@400;600;700&family=Roboto:wght@400&display=swap">
<style>
  :root {
    --page: #e9ecea;
    --card: #e3e7e3;
    --card-edge: #cfd6d2;
    --teal: #1f968b;
    --teal-band: #2aa597;
    --orange: #d98a2f;
    --ink: #1e3b3a;
    --icon-bg: #e8dcc0;
  }
  * { box-sizing: border-box; margin: 0; padding: 0; }
  html, body { width: 1200px; height: 952px; overflow: hidden; }
  body {
    background: var(--page);
    display: flex;
    flex-direction: column;
    align-items: center;
    justify-content: center;
    gap: 52px;
  }
  .card {
    position: relative;
    width: 700px;
    height: 400px;
    background: var(--card);
    border: 1px solid var(--card-edge);
    border-radius: 6px;
    overflow: hidden;
    box-shadow: 0 6px 18px rgba(30, 59, 58, 0.12);
  }
  .identity {
    position: absolute;
    font-family: "Cinzel", serif;
  }
  .identity__name {
    color: var(--teal);
    font-weight: 700;
    white-space: nowrap;
    line-height: 1;
  }
  .identity__name .honorific { font-size: 0.62em; }
  .identity__name .credential { font-size: 0.5em; vertical-align: 0.7em; margin-left: 4px; }
  .identity__title {
    color: var(--orange);
    font-weight: 400;
    white-space: nowrap;
    margin-top: 4px;
  }
  .card--front .identity { left: 120px; top: 160px; }
  .card--front .identity__name { font-size: 52px; }
  .card--front .identity__title { font-size: 27px; }

  .card--back .identity { left: 40px; top: 40px; z-index: 2; }
  .card--back .identity__name { font-size: 40px; }
  .card--back .identity__title { font-size: 21px; }

  .swoosh { position: absolute; inset: 0; width: 100%; height: 100%; }

  .contact {
    position: absolute;
    left: 360px;
    top: 250px;
    list-style: none;
    font-family: "Roboto", sans-serif;
    font-size: 19px;
    color: var(--ink);
    line-height: 1.25;
  }
  .contact__item { display: flex; align-items: flex-start; gap: 10px; margin-bottom: 8px; }
  .contact__icon { flex: none; width: 20px; height: 20px; margin-top: 2px; }
</style>
</head>
<body>

<section class="card card--front" aria-label="Business card front">
  <div class="identity">
    <p class="identity__name"><span class="honorific">Dr.</span>Laurel Hayes<span class="credential">Ph.D.</span></p>
    <p class="identity__title">Licensed Clinical Psychologist</p>
  </div>
</section>

<section class="card card--back" aria-label="Business card back">
  <svg class="swoosh" viewBox="0 0 700 400" aria-hidden="true">
    <path d="M0 400 C210 330 430 150 640 0 L700 0 L700 400 Z" fill="var(--orange)"/>
    <path d="M245 400 C330 220 490 70 700 12 L700 400 Z" fill="var(--teal-band)"/>
  </svg>
  <div class="identity">
    <p class="identity__name"><span class="honorific">Dr.</span>Laurel Hayes<span class="credential">Ph.D.</span></p>
    <p class="identity__title">Licensed Clinical Psychologist</p>
  </div>
  <ul class="contact">
    <li class="contact__item">
      <svg class="contact__icon" viewBox="0 0 20 20" aria-hidden="true">
        <rect width="20" height="20" rx="2" fill="var(--icon-bg)"/>
        <path d="M6 4 L8.5 4 L9.5 7 L8 8.3 C8.8 10 10 11.2 11.7 12 L13 10.5 L16 11.5 L16 14 C16 15 15 16 14 16 C8.5 15.5 4.5 11.5 4 6 C4 5 5 4 6 4 Z" fill="var(--teal)"/>
      </svg>
      <span>312-555-0148</span>
    </li>
    <li class="contact__item">
      <svg class="contact__icon" viewBox="0 0 20 20" aria-hidden="true">
        <rect width="20" height="20" rx="2" fill="var(--icon-bg)"/>
        <rect x="4" y="6" width="12" height="9" fill="none" stroke="var(--teal)" stroke-width="1.5"/>
        <path d="M4 6 L10 11 L16 6" fill="none" stroke="var(--teal)" stroke-width="1.5"/>
      </svg>
      <span>Drlaurelhayes@mail.com</span>
    </li>
    <li class="contact__item">
      <svg class="contact__icon" viewBox="0 0 20 20" aria-hidden="true">
        <rect width="20" height="20" rx="2" fill="var(--icon-bg)"/>
        <path d="M10 3.5 C7.2 3.5 5.5 5.5 5.5 8 C5.5 11 10 16.5 10 16.5 C10 16.5 14.5 11 14.5 8 C14.5 5.5 12.8 3.5 10 3.5 Z" fill="var(--teal)"/>
        <circle cx="10" cy="8" r="1.8" fill="var(--icon-bg)"/>
      </svg>
      <span>240 N. Larkin Suite 908<br>Chicago, Illinois 60601</span>
    </li>
  </ul>
</section>

</body>
</html>
```